Homes, Invest in Non-performing loans

We need only 3 web pages, one for the home, one for the content, one for the properties.
The main focus of our business is to offer non performing loans (before foreclosures) to the general public. All the non-performing mortgages will end in a house, an apartment, a store, etc.
Our customers are able to invest from 10,000usd to 1,000,000usd (average 50,000usd).
Our customers' usual focus groups are employees who want second earnings, perceiving the business feeling without outlay time. They look for a solid finance sense corporation that confers them certainty.
Nearly all our clients desire the house, apartment, store, etc. more than the actual earnings.
The name of our company is BRAMLEY
Reason: We value the time and effort you already invest in our project. We realize that we did't come back on some of the doubts requested by the designers. It will be inequitable to the designers who prerequisite our feedback. We also appreciate the comprehension of the community in this postponement.
Reason: Designers,
We really apreciate all the time and effort you put on our project. From the begining we ask for 3 pages, so now we will leave the 10 finalist and provide some extra time to submit the other 2 pages.
We will race the price in 10%
Target Market(s)
Our customers average investors works as employees and want to have a second income or business without spending time. (People from 35 to 50)
Industry/Entity Type
Finance
Requirements
Should not have
- FLASH

```html
<!DOCTYPE html>
<html lang="en">
<head>
<meta charset="utf-8">
<title>Bramley – Home</title>
<link rel="stylesheet" href="https://fonts.googleapis.com/css2?family=Source+Sans+3:ital,wght@0,400;0,600;0,700;1,800;1,900&family=Arimo:wght@400;700&display=swap">
<style>
:root{
  --olive:#8a8420;
  --olive-dark:#6d6812;
  --olive-light:#a29c2c;
  --band-grey:#adabad;
  --dark:#434343;
  --text:#4a4a4a;
  --heading:#3d3d3d;
  --white:#ffffff;
  --muted:#d8d8d8;
}
*{box-sizing:border-box;margin:0;padding:0}
html,body{width:1180px;height:1200px;overflow:hidden;background:var(--white)}
body{position:relative;font-family:"Source Sans 3",sans-serif;color:var(--text)}
.abs{position:absolute}

/* header */
.brand{left:199px;top:40px;display:flex;align-items:center;gap:8px}
.brand-mark{width:20px;height:20px;background:var(--olive)}
.brand-name{font-size:30px;font-weight:700;color:#3a3a3a;letter-spacing:1px}
.phone{left:815px;top:78px;font-size:16px;color:#333;display:flex;align-items:center;gap:8px}

/* grey hero band */
.hero-band{left:0;top:140px;width:1180px;height:420px;background:var(--band-grey)}

/* navigation */
.main-nav{left:167px;top:111px;width:846px;height:51px;border-radius:3px;
  background:linear-gradient(#9a942a,#7d7819);display:flex;align-items:center;padding-left:10px}
.main-nav a{color:var(--white);text-decoration:none;font-size:16px;padding:0 23px;line-height:51px;
  border-right:1px solid rgba(0,0,0,.15)}
.main-nav a:nth-child(6){border-right:none}
.search{position:absolute;left:600px;top:10px;width:215px;height:32px;background:var(--olive-dark);
  color:var(--white);font-size:10px;display:flex;align-items:center;justify-content:space-between;padding:0 12px 0 17px}

/* slider */
.slider{left:193px;top:181px;width:795px;height:346px;background:var(--white);border-radius:4px;
  box-shadow:0 14px 14px -10px rgba(0,0,0,.35)}
.slide-photo{position:absolute;left:17px;top:16px;width:761px;height:314px;
  background:linear-gradient(110deg,#e8e6e3 0%,#d9c8b6 35%,#e9dccb 55%,#f1ede6 80%,#e4e1dc 100%)}
.slide-arrow{position:absolute;top:140px}
.slide-title{position:absolute;right:33px;top:190px;text-align:right;font-style:italic;line-height:.95}
.slide-title .l1{font-size:38px;font-weight:900;color:var(--white)}
.slide-title .l2{font-size:44px;font-weight:900;color:var(--olive)}
.slide-title .l3{font-size:24px;font-weight:800;color:var(--white)}

/* intro sections */
.section-title{font-size:28px;font-weight:400;color:var(--heading)}
.body-text{font-size:10.5px;line-height:12.6px;text-align:justify}
.body-text p+p{margin-top:12px}
.service-list{list-style:none;font-size:10.5px;margin-top:14px}
.service-list li{margin-bottom:13px}
.service-list li::before{content:"> ";}
.btn{display:inline-block;background:linear-gradient(#9a942a,#746f15);color:var(--white);font-size:12.5px;
  width:95px;height:30px;line-height:30px;text-align:center;border-radius:2px;text-decoration:none}

/* dark band */
.dark-band{left:0;top:855px;width:1180px;height:266px;background:var(--dark)}
.dark-band .section-title{color:#e4e4e4}
.view-link{font-size:12px;color:#e6e6e6}
.quote-card{position:absolute;top:63px;width:220px;height:168px;background:var(--white);border:1px solid #ccc;
  border-radius:2px;padding:14px 10px 0 65px;font-family:"Arimo",sans-serif;font-size:10.3px;line-height:10.7px;color:#444}
.avatar{position:absolute;left:10px;top:14px;width:47px;height:47px;border:1px solid #ccc;background:linear-gradient(#f1f1f1,#cfcfcf)}
.quote-card p+p{margin-top:10px}
.quote-author{margin-top:12px;font-weight:700}
.news-item{position:absolute;left:0;display:flex;gap:14px}
.news-date{width:41px;height:36px;background:linear-gradient(#a29c2c,#7d7819);color:#fff;text-align:center;
  border-radius:2px;font-size:13px;line-height:14px;padding-top:4px;flex:none}
.news-date small{display:block;font-size:7.5px}
.news-text{font-size:10px;line-height:12.5px;color:#ddd;width:230px}

/* footer */
.footer-nav{left:199px;top:1144px;font-size:12px;color:#333}
.footer-nav span{margin:0 5px;color:#666}
.copyright{left:199px;top:1163px;font-size:12px;color:#333}
.social{left:786px;top:1146px;display:flex;align-items:center;gap:5px;font-size:11px;color:#333}
.social .label{margin-right:12px}
.social i{width:26px;height:26px;border-radius:50%;background:#4b4b4b;display:block}
</style>
</head>
<body>

<header>
  <div class="abs brand"><span class="brand-mark"></span><span class="brand-name">BRAMLEY</span></div>
  <div class="abs phone">
    <svg width="14" height="18" viewBox="0 0 14 18"><path d="M9 1 L12 3 L9 7 L7 6 C5 9 5 12 7 14 L9 12 L12 14 L10 17 C4 17 1 10 9 1Z" fill="#333"/></svg>
    Phone - 01632 960418
  </div>
</header>

<div class="abs hero-band"></div>

<nav class="abs main-nav">
  <a>Home</a><a>About</a><a>Services</a><a>Loans</a><a>Testimonial</a><a>Contact</a>
  <div class="search">Enter Keywords
    <svg width="12" height="12" viewBox="0 0 12 12"><circle cx="5" cy="5" r="3.5" stroke="#fff" stroke-width="1.8" fill="none"/><path d="M7.5 7.5 L11 11" stroke="#fff" stroke-width="2"/></svg>
  </div>
</nav>

<section class="abs slider">
  <div class="slide-photo" role="img" aria-label="Photo of a smiling family of four relaxing together at home"></div>
  <svg class="slide-arrow" style="left:57px" width="32" height="66" viewBox="0 0 32 66"><path d="M30 0 L4 33 L30 66 L22 66 L0 33 L22 0Z" fill="#8f8f8f" opacity=".8"/></svg>
  <svg class="slide-arrow" style="left:715px" width="32" height="66" viewBox="0 0 32 66"><path d="M2 0 L28 33 L2 66 L10 66 L32 33 L10 0Z" fill="#8f8f8f" opacity=".8"/></svg>
  <div class="slide-title"><div class="l1">LORE</div><div class="l2">COMMOD</div><div class="l3">AE MASSAA</div></div>
</section>

<section class="abs" style="left:193px;top:583px;width:459px">
  <h2 class="section-title">Welcome to Our Site</h2>
  <div class="body-text" style="margin-top:22px">
    <p>Lorem ipsum dolor sit amet, consectetuer adipiscing elit. Aenean commodo ligula eget dolor. Aenean massa. Cum sociis natoque penatibus et magnis dis parturient montes, nascetur ridiculus mus. Donec quam felis, ultricies nec, pellentesque eu, pretium quis, sem. Nulla consequat massa quis enim. Donec pede justo, fringilla vel, aliquet nec, vulputate eget, arcu.</p>
    <p>In enim justo, rhoncus ut, imperdiet a, venenatis vitae, justo. Nullam dictum felis eu pede mollis pretium. Integer tincidunt. Cras dapibus. Vivamus elementum semper nisi. Aenean vulputate eleifend tellus. Aenean leo ligula, porttitor eu, consequat vitae, eleifend ac, enim. Aliquam lorem ante, dapibus in, viverra quis, feugiat a, tellus.Lorem ipsum dolor sit amet, consectetuer adipiscing elit. Aenean commodo ligula eget dolor. Aenean massa. Cum sociis natoque penatibus et magnis dis parturient montes, nascetur ridiculus mus. Donec quam felis, ultricies nec, pellentesque eu, pretium quis, sem.</p>
  </div>
</section>
<a class="abs btn" style="left:193px;top:802px">View More</a>

<section class="abs" style="left:694px;top:583px;width:285px">
  <h2 class="section-title">Our Services</h2>
  <p class="body-text" style="margin-top:22px;text-align:left">Lorem ipsum dolor sit amet, consectetuer adipiscing elit. Aenean commodo ligula eget dolor. Aenean massa. Cum sociis natoque penatibus et magnis dis parturient montes,</p>
  <ul class="service-list">
    <li>Donec pede justo, fringilla vel, aliquet nec, vulputate eget</li>
    <li>Nullam dictum felis eu pede mollis pretium.</li>
    <li>Integer tincidunt. Cras dapibus. Vivamus elementum semper</li>
    <li>Aenean leo ligula, porttitor eu, consequat vitae</li>
  </ul>
</section>
<a class="abs btn" style="left:696px;top:802px">View More</a>

<section class="abs dark-band">
  <h2 class="abs section-title" style="left:193px;top:20px">Testimonial</h2>
  <span class="abs view-link" style="left:592px;top:34px">View More...</span>
  <div class="quote-card" style="left:197px">
    <div class="avatar" role="img" aria-label="Portrait of the client"></div>
    <p>Lorem ipsum dos siconipiscing elit. Etiam commodo ante non nequ bibendumtristique.gestas in imperdiet sed, Lorem ipdolor sit m,conipiscing .</p>
    <p>Etommodo ante non neque bibendum tristique. Vestibulum nulldiam, egestas in imperdiet sedLorem ipsusm,conipiscing elit. Etiam commodo</p>
    <p class="quote-author">Sam Carter</p>
  </div>
  <div class="quote-card" style="left:432px">
    <div class="avatar" role="img" aria-label="Portrait of the client"></div>
    <p>Lorem ipsum dos siconipiscing elit. Etiam commodo ante non nequ bibendumtristique.gestas in imperdiet sed, Lorem ipdolor sit m,conipiscing .</p>
    <p>Etommodo ante non neque bibendum tristique. Vestibulum nulldiam, egestas in imperdiet sedLorem ipsusm,conipiscing elit. Etiam commodo</p>
    <p class="quote-author">Sam Carter</p>
  </div>

  <h2 class="abs section-title" style="left:694px;top:20px">Latest News</h2>
  <div class="abs" style="left:694px;top:63px;width:290px;height:200px">
    <div class="news-item" style="top:0"><div class="news-date">30<small>Nov '12</small></div>
      <p class="news-text">Lorem ipsum dolor sit amet, consectetuer adipiscing elit. Aenean commodo ligula eget dolor. Aenean mas Cum sociis natoque penatibus et magnis dis pmonte Lorem ipsum dolor sit amet, consectetuer</p></div>
    <div class="news-item" style="top:67px"><div class="news-date">30<small>Nov '12</small></div>
      <p class="news-text">Lorem ipsum dolor sit amet, consectetuer adipiscing elit. Aenean commodo ligula eget dolor. Aenean mas Cum sociis natoque penatibus et magnis dis pmonte Lorem ipsum dolor sit amet, consectetuer</p></div>
    <a class="btn" style="position:absolute;left:0;top:149px">View More</a>
  </div>
</section>

<footer>
  <div class="abs footer-nav">Home<span>|</span>About Us<span>|</span>Careers<span>|</span>Terms &amp; Conditions<span>|</span>Contact</div>
  <div class="abs copyright">Copyright © 2012. All Rights Reserved.</div>
  <div class="abs social"><span class="label">Social Media:</span><i></i><i></i><i></i><i></i></div>
</footer>

</body>
</html>
```